BrightPath Medical Exercise, LLC specializes in post rehab medical exercise for clients who have been discharged from physical therapy and/or other medical services and are in need of continued cardiovascular, strength, flexibility, endurance training and management of their medical conditions. We strive to bridge the gap between healthcare and fitness by staying in communication with the referring physician and /or physical therapist with updated progress notes to follow each clients progression, making sure each client is appropriate for exercise and identifying any red flags throughout the initial assessment and screening of the client, and referring those clients back to the physician and/or therapist when necessary.
Colors
Designer to choose colors to be used in the design.
Requirements
Must have
- Pictures of a trainer working with a client one on one during exercise, and group exercise
Nice to have
- Pictures that portray the bridge between healthcare and fitness
Should not have
- Cursive writing

```html
<!DOCTYPE html>
<html lang="en">
<head>
<meta charset="utf-8">
<title>BrightPath Medical Exercise – Rack Card</title>
<link href="https://fonts.googleapis.com/css2?family=Lato:ital,wght@0,400;0,700;0,900;1,400;1,700&display=swap" rel="stylesheet">
<style>
:root{
  --red:#e8392a;
  --red-deep:#d42a1f;
  --navy:#13203f;
  --gray:#4f5053;
  --ink:#222326;
  --white:#ffffff;
  --stage:#e9e9ea;
}
*{box-sizing:border-box;margin:0;padding:0}
html,body{width:708px;height:1200px;overflow:hidden;background:var(--stage);font-family:'Lato',Arial,sans-serif;color:var(--ink)}
.canvas{position:relative;width:708px;height:1200px}
.card{position:absolute;top:230px;width:330px;height:740px;background:var(--white);overflow:hidden;box-shadow:6px 8px 18px rgba(0,0,0,.28)}
.card--front{left:16px}
.card--back{left:362px}
.abs{position:absolute}
.photo-trainer{left:0;top:0;width:330px;height:240px;background:linear-gradient(160deg,#f1ece6 0%,#e4d7cb 45%,#b9a796 100%)}
.deco{position:absolute;left:0;top:0}
.brand{left:150px;top:350px;width:170px;display:flex;align-items:center;justify-content:center;gap:6px}
.brand-dot{width:10px;height:10px;border-radius:50%;background:var(--red)}
.brand-name{font-weight:900;font-size:10px;color:var(--ink);text-transform:uppercase;line-height:1.1;text-align:center}
.headline{left:0;top:398px;width:330px;text-align:center;color:var(--red);font-weight:700;font-size:18.5px;line-height:1.12;letter-spacing:-.2px}
.svc{color:var(--white);font-size:9px;line-height:1.3;text-align:center}
.svc--one{left:104px;top:520px;width:120px}
.svc--assess{left:42px;top:604px;width:88px}
.svc--online{left:154px;top:628px;width:116px}
.svc-center{left:126px;top:574px;width:74px;text-align:center;font-weight:900;font-size:10px;line-height:1.15;color:var(--ink)}
.web{left:0;top:708px;width:330px;text-align:center;color:var(--white);font-size:13px;display:flex;justify-content:center;align-items:center;gap:6px}
.web-dot{width:9px;height:9px;border:1.5px solid var(--white);border-radius:50%}
.quote{left:32px;top:48px;width:280px;font-style:italic;font-size:13px;line-height:1.4;color:var(--ink)}
.quote-mark{font-size:26px;font-weight:900;color:var(--ink);line-height:1}
.quote-mark--open{left:18px;top:34px}
.quote-mark--close{left:296px;top:100px}
.author{left:186px;top:80px;width:130px;font-style:italic;font-weight:700;font-size:12px}
.author small{display:block;font-style:normal;font-weight:400;font-size:8px;margin-left:14px}
.photo-bottle{left:46px;top:122px;width:144px;height:144px;border-radius:50%;background:radial-gradient(circle at 50% 60%,#3a5fa8 0%,#5b6f7e 45%,#9a8a70 100%);border:3px solid var(--white)}
.photo-bands{left:172px;top:175px;width:94px;height:94px;border-radius:50%;background:radial-gradient(circle at 45% 45%,#c9cdd2 0%,#8c96a1 50%,#3c4550 100%);border:3px solid var(--white)}
.conditions-title{left:20px;top:291px;width:300px;color:var(--red);font-weight:700;font-size:10.5px}
.conditions{left:22px;top:313px;width:300px;display:grid;grid-template-columns:143px 157px;list-style:none}
.conditions li{font-size:10.2px;line-height:18.6px;display:flex;align-items:center;gap:7px;white-space:nowrap}
.conditions li::before{content:"";width:6px;height:6px;border:1.2px solid var(--red);border-radius:50%;flex:none}
.phone{left:0;top:598px;width:330px;display:flex;justify-content:center;align-items:center;gap:10px;font-size:27px;color:var(--ink)}
.email{left:0;top:638px;width:330px;text-align:center;font-size:13px;display:flex;justify-content:center;align-items:center;gap:6px}
.social{left:0;top:660px;width:330px;display:flex;justify-content:center;gap:12px}
.social span{width:20px;height:20px;border:1.4px solid var(--ink);border-radius:50%}
</style>
</head>
<body>
<div class="canvas">

  <!-- Front -->
  <section class="card card--front">
    <div class="abs photo-trainer" role="img" aria-label="Photo of a trainer guiding a client through a resistance band exercise"></div>
    <svg class="deco" width="330" height="740" viewBox="0 0 330 740" aria-hidden="true">
      <path d="M0 232 C60 222 130 250 168 300 C120 268 60 256 0 258Z" fill="var(--navy)"/>
      <path d="M0 245 C100 200 240 190 330 210 L330 240 L330 203 C240 176 100 190 0 245Z" fill="var(--white)"/>
      <path d="M34 292 C110 230 240 205 330 222" fill="none" stroke="var(--red)" stroke-width="5"/>
      <circle cx="164" cy="530" r="70" fill="var(--navy)" stroke="var(--white)" stroke-width="3"/>
      <circle cx="88" cy="622" r="54" fill="var(--red)" stroke="var(--white)" stroke-width="3"/>
      <circle cx="210" cy="614" r="66" fill="var(--gray)" stroke="var(--white)" stroke-width="3"/>
      <circle cx="163" cy="588" r="38" fill="var(--white)"/>
      <path d="M0 700 C100 684 230 684 330 700 L330 740 L0 740Z" fill="var(--red)"/>
    </svg>
    <div class="abs brand"><span class="brand-dot"></span><span class="brand-name">BrightPath<br>Medical Exercise</span></div>
    <h1 class="abs headline">Getting You Back To Function As<br>Quickly And Safely As Possible</h1>
    <p class="abs svc svc--one">One-On-One supervised<br>post rehab exercise</p>
    <p class="abs svc-center">Our Products and Services:</p>
    <p class="abs svc svc--assess">Initial Assessment and Functional Screening</p>
    <p class="abs svc svc--online">Online consultation with individualized home exercise program</p>
    <p class="abs web"><span class="web-dot"></span>www.brightpathmedex.com</p>
  </section>

  <!-- Back -->
  <section class="card card--back">
    <svg class="deco" width="330" height="740" viewBox="0 0 330 740" aria-hidden="true">
      <path d="M12 100 V24 H112" fill="none" stroke="var(--red)" stroke-width="1.5"/>
      <path d="M318 24 V100 H250" fill="none" stroke="var(--red)" stroke-width="1.5"/>
      <path d="M0 190 C70 110 220 100 300 140" fill="none" stroke="var(--red)" stroke-width="4"/>
      <path d="M10 200 C80 130 200 120 280 150" fill="none" stroke="var(--red)" stroke-width="2"/>
      <path d="M30 268 C120 290 240 285 300 210" fill="none" stroke="var(--red)" stroke-width="2"/>
      <path d="M70 590 C170 604 280 592 326 546" fill="none" stroke="var(--red)" stroke-width="3" opacity=".8"/>
      <path d="M0 700 C100 684 230 684 330 700 L330 740 L0 740Z" fill="var(--red)"/>
    </svg>
    <span class="abs quote-mark quote-mark--open">“</span>
    <p class="abs quote">Exercise is the key to long-term management of most medical conditions</p>
    <p class="abs author">~ Daniel R Hayes,<small>PhD, PT</small></p>
    <span class="abs quote-mark quote-mark--close">”</span>
    <div class="abs photo-bottle" role="img" aria-label="Photo of dumbbells and a water bottle on a wooden deck"></div>
    <div class="abs photo-bands" role="img" aria-label="Photo of coiled resistance tubes"></div>
    <h2 class="abs conditions-title">We offer management of the following conditions and more:</h2>
    <ul class="abs conditions">
      <li>Diabetes</li><li>AC Joint Separation</li>
      <li>Hypertension</li><li>Fibromyalgia</li>
      <li>ACL Rupture</li><li>Spondylothesis</li>
      <li>Ankle Fracture</li><li>Parkinson's Disease</li>
      <li>Bicipital Tendonitis</li><li>Tibial Plateau Fracture</li>
      <li>Total Hip Replacement</li><li>Tennis Elbow/Golfer's Elbow</li>
      <li>Total Knee Replacement</li><li>Carpal Tunnel Syndrome</li>
      <li>Spinal Stenosis</li><li>Total Shoulder Replacement</li>
      <li>Multiple Sclerosis</li><li>Bicipital Tendonitis</li>
      <li>Shoulder Dislocation</li><li>Patello-Femoral Syndrome</li>
      <li>Scoliosis</li><li>Rotator Cuff Syndrome</li>
      <li>Osteoporosis</li><li>Cervical Strain</li>
      <li>Osteoarthritis</li><li>Impingement Syndrome</li>
      <li>Cervical disc herniation</li><li>Laminectomy</li>
    </ul>
    <p class="abs phone">
      <svg width="28" height="28" viewBox="0 0 28 28" aria-hidden="true"><circle cx="14" cy="14" r="12.5" fill="none" stroke="var(--red)" stroke-width="2.5"/><path d="M9 8 L12 8 L13 11 L11.5 12.5 C12.5 14.5 13.5 15.5 15.5 16.5 L17 15 L20 16 L20 19 C14 19.5 8.5 14 9 8Z" fill="var(--red)"/></svg>
      (555) 014-7302
    </p>
    <p class="abs email">
      <svg width="11" height="8" viewBox="0 0 11 8" aria-hidden="true"><rect x=".5" y=".5" width="10" height="7" fill="none" stroke="var(--red)"/><path d="M.5 .5 L5.5 4.5 L10.5 .5" fill="none" stroke="var(--red)"/></svg>
      brightpathmedex@mail.com
    </p>
    <div class="abs social"><span></span><span></span><span></span></div>
    <p class="abs web"><span class="web-dot"></span>www.brightpathmedex.com</p>
  </section>

</div>
</body>
</html>
```